Vantor Ridge needs a Business Card Design

We need a business card design for an Information Technology company based in Fairfax Virginia called Vantor Ridge. We want the business card to use our logo colors. We need it to be double-sided. The business card needs to look professional but we would like it to be unique. You can get company information from our web site (http://www.vantorridgellc.example).

Target Market(s)

Target market is Government Agencies and Business Professionals.

Industry/Entity Type

Business

Requirements
Must have
• Must have section for company name, company address, company URL, employee name, title, phone and email. Also must have company logo and space for entering logos.

```html
<!DOCTYPE html>
<html lang="en">
<head>
<meta charset="utf-8">
<title>Vantor Ridge – Business Card</title>
<link rel="stylesheet" href="https://fonts.googleapis.com/css2?family=Questrial&family=Tinos&display=swap">
<style>
  :root {
    --page-bg: #e9e6e1;
    --front-dark: #1f2427;
    --front-mid: #5c6164;
    --front-edge: #2b2f32;
    --brand-lavender: #8797ef;
    --brand-square: #3d55d8;
    --tagline-grey: #9ba1a5;
    --placeholder-violet: #7c86f2;
    --url-cyan: #52d3f2;
    --back-blue: #0c74c2;
    --back-glow: #22b8ec;
    --back-ink: #1c3b8e;
  }
  * { margin: 0; padding: 0; box-sizing: border-box; }
  html, body {
    width: 1200px;
    height: 1200px;
    overflow: hidden;
    background: var(--page-bg);
  }
  .canvas {
    position: relative;
    width: 1200px;
    height: 1200px;
  }
  .card {
    position: absolute;
    left: 162px;
    width: 875px;
    height: 500px;
    overflow: hidden;
    box-shadow: 0 6px 18px rgba(0,0,0,0.18);
  }

  /* Back side */
  .card--back {
    top: 70px;
    background: var(--back-blue);
    box-shadow: inset 0 0 40px 10px var(--back-glow), 0 6px 18px rgba(0,0,0,0.18);
  }
  .holder-name {
    position: absolute;
    left: 90px;
    top: 120px;
    font-family: "Tinos", serif;
    font-size: 44px;
    letter-spacing: 1px;
    color: var(--back-ink);
  }
  .holder-title {
    position: absolute;
    left: 150px;
    top: 168px;
    font-family: "Tinos", serif;
    font-size: 28px;
    letter-spacing: 1px;
    color: var(--back-ink);
  }
  .holder-contact {
    position: absolute;
    left: 480px;
    top: 250px;
    font-family: "Questrial", sans-serif;
    font-size: 22px;
    line-height: 1.35;
    letter-spacing: 1px;
    color: var(--back-ink);
  }

  /* Front side */
  .card--front {
    top: 630px;
    background: linear-gradient(100deg, var(--front-dark) 0%, var(--front-dark) 18%, var(--front-mid) 55%, var(--front-edge) 100%);
  }
  .brand {
    position: absolute;
    left: 225px;
    top: 120px;
    display: flex;
    align-items: center;
    gap: 18px;
  }
  .brand-square {
    width: 48px;
    height: 48px;
    background: var(--brand-square);
  }
  .brand-name {
    font-family: "Questrial", sans-serif;
    font-size: 54px;
    letter-spacing: 1px;
    color: var(--brand-lavender);
  }
  .tagline {
    position: absolute;
    left: 291px;
    top: 184px;
    font-family: "Questrial", sans-serif;
    font-size: 15px;
    letter-spacing: 1.5px;
    color: var(--tagline-grey);
  }
  .details {
    position: absolute;
    left: 250px;
    top: 228px;
    font-family: "Questrial", sans-serif;
    font-size: 21px;
    line-height: 1.3;
    letter-spacing: 1px;
    color: var(--placeholder-violet);
  }
  .site-url {
    position: absolute;
    left: 190px;
    top: 340px;
    font-family: "Questrial", sans-serif;
    font-size: 28px;
    letter-spacing: 1px;
    color: var(--url-cyan);
  }
</style>
</head>
<body>
  <main class="canvas">
    <section class="card card--back" aria-label="Card back">
      <p class="holder-name">YOUR NAME</p>
      <p class="holder-title">TITLE</p>
      <div class="holder-contact">
        <p>PH : 444-555-555</p>
        <p>EMAIL: YOURMAIL@YOUR.COM</p>
      </div>
    </section>

    <section class="card card--front" aria-label="Card front">
      <div class="brand">
        <span class="brand-square" aria-hidden="true"></span>
        <span class="brand-name">Vantor Ridge</span>
      </div>
      <p class="tagline">TURNING IDEAS INTO RELIABLE SYSTEMS</p>
      <div class="details">
        <p>XXXXX XXXXX XXXXXX</p>
        <p>XXXXX XXXX</p>
        <p>XXXXX - 55554444</p>
      </div>
      <p class="site-url">WWW.YOURSITE.COM</p>
    </section>
  </main>
</body>
</html>
```